New Plumbing Company

We are looking for a smart and creative business card design for our new plumbing company. We are looking for creativity and originality in our business cards.

Industry/Entity Type

Plumbing

Contact Information for Business Card

Crestline Plumbing
Peter Halvane
Managing Director
Telephone Number : 0481529604
Email : service@crestlineplumbing.com.au
Website : www.crestlineplumbing.com.au
Lic. 508264K

Colors
0692cd
33a6d7
000000

Requirements
Must have
• I want the business card to be designed on a black background using the blue tones i have selected as seen in the company logo.

```html
<!DOCTYPE html>
<html lang="en">
<head>
<meta charset="utf-8">
<title>Crestline Plumbing – Business Card</title>
<link href="https://fonts.googleapis.com/css2?family=Roboto:wght@400;500&display=swap" rel="stylesheet">
<style>
  :root {
    --ink: #0a0a0c;
    --blue: #1790cf;
    --sky: #a6d6ec;
    --white: #ffffff;
    --paper: #ffffff;
    --muted: #d8d8d8;
    --ghost: #1c1c1f;
  }
  * { margin: 0; padding: 0; box-sizing: border-box; }
  html, body { width: 1200px; height: 800px; overflow: hidden; background: var(--paper); }
  body { position: relative; font-family: "Roboto", Arial, sans-serif; color: var(--white); }

  .card { position: absolute; top: 293px; width: 449px; height: 262px; }
  .card--front { left: 148px; }
  .card--back { left: 610px; width: 448px; }
  .card__shapes { position: absolute; inset: 0; width: 100%; height: 100%; }

  .brand { position: absolute; display: flex; align-items: center; white-space: nowrap; }
  .brand__dot { border-radius: 50%; border: 3px solid var(--blue); flex: none; }
  .brand__name { color: var(--white); font-weight: 400; }

  .brand--front { left: 130px; top: 106px; gap: 12px; }
  .brand--front .brand__dot { width: 40px; height: 40px; }
  .brand--front .brand__name { font-size: 25px; letter-spacing: 0.5px; }

  .brand--back { left: 36px; top: 36px; gap: 8px; }
  .brand--back .brand__dot { width: 24px; height: 24px; border-width: 2px; }
  .brand--back .brand__name { font-size: 15px; }

  .person { position: absolute; right: 255px; top: 102px; text-align: right; }
  .person__name { font-size: 17px; font-weight: 400; line-height: 1; }
  .person__role { font-size: 8.5px; color: var(--muted); margin-top: 5px; }

  .divider { position: absolute; left: 220px; top: 98px; width: 1px; height: 54px; background: #666; }

  .contacts { position: absolute; left: 207px; top: 100px; list-style: none; }
  .contacts li { display: flex; align-items: center; height: 15px; font-size: 10px; }
  .contacts svg { width: 8px; height: 8px; margin-right: 13px; flex: none; }

  .licence { position: absolute; left: 175px; top: 242px; font-size: 8px; color: var(--white); }
</style>
</head>
<body>

<section class="card card--front" aria-label="Business card front">
  <svg class="card__shapes" viewBox="0 0 449 262" aria-hidden="true">
    <polygon points="145,0 449,0 449,194 392,262 0,262 0,121" fill="var(--ink)"/>
    <polygon points="0,0 114,0 0,95" fill="var(--blue)"/>
    <circle cx="35" cy="30" r="15" fill="none" stroke="var(--white)" stroke-width="2"/>
    <polygon points="0,262 392,262 449,194" fill="var(--blue)"/>
  </svg>
  <div class="brand brand--front">
    <span class="brand__dot"></span>
    <span class="brand__name">Crestline Plumbing</span>
  </div>
</section>

<section class="card card--back" aria-label="Business card back">
  <svg class="card__shapes" viewBox="0 0 448 262" aria-hidden="true">
    <rect x="0" y="0" width="448" height="262" fill="var(--ink)"/>
    <circle cx="340" cy="160" r="60" fill="none" stroke="var(--ghost)" stroke-width="4"/>
    <polygon points="305,0 333,0 448,94 448,120" fill="var(--sky)"/>
    <polygon points="333,0 448,0 448,94" fill="var(--blue)"/>
    <circle cx="414" cy="32" r="15" fill="none" stroke="var(--white)" stroke-width="2"/>
    <polygon points="0,193 448,260 448,262 55,262" fill="var(--blue)"/>
  </svg>
  <div class="brand brand--back">
    <span class="brand__dot"></span>
    <span class="brand__name">Crestline Plumbing</span>
  </div>
  <div class="person">
    <p class="person__name">Peter Halvane</p>
    <p class="person__role">Managing Director</p>
  </div>
  <span class="divider"></span>
  <ul class="contacts">
    <li><svg viewBox="0 0 8 8"><rect x="2" y="0" width="4" height="8" rx="1" fill="var(--white)"/></svg>0481529604</li>
    <li><svg viewBox="0 0 8 8"><rect x="0" y="1.5" width="8" height="5" fill="var(--white)"/><polyline points="0,1.5 4,4.5 8,1.5" fill="none" stroke="var(--ink)" stroke-width="0.8"/></svg>service@crestlineplumbing.com.au</li>
    <li><svg viewBox="0 0 8 8"><circle cx="4" cy="4" r="3.6" fill="var(--white)"/><path d="M0.5 4H7.5M4 0.5V7.5" stroke="var(--ink)" stroke-width="0.7"/></svg>www.crestlineplumbing.com.au</li>
  </ul>
  <p class="licence">Lic. 508264K</p>
</section>

</body>
</html>
```